Entertainment Sound and Lighting company Business card

We need a professional looking business card designed for my growing entertainment sound and lighting company based in Sydney, Australia called "Kestrel Sound"

We provide technical production services (sound systems/lighting/vision) for events ranging from band gigs, weddings, corporate functions etc.

The business card needs to contain the following information:

Bartholomew Quenneville
Audio Engineer
Phone: 0478 615 027
Email: bartholomew@kestrelsound.com.au
Website: www.kestrelsound.com.au

Business logo has been attached in .ai format, please contact me if you need me to provide other files.

Target Market(s)

We need a business card that reflects our modern and professional company but still looks professional to appeal to our corporate clients.
We have a very broad target market spanning from bands needing PA systems for their gigs (18-30yrs) to event companies needing sound and lighting for weddings and other functions.

Industry/Entity Type

Business

Requirements
Must have
• Needs to include the logo that is attached of course, and the colour scheme.
Nice to have
• - Double sided

```html
<!DOCTYPE html>
<html lang="en">
<head>
<meta charset="utf-8">
<title>Kestrel Sound — Business Card Print Sheet</title>
<link rel="stylesheet" href="https://fonts.googleapis.com/css2?family=Barlow:wght@400;500;700;800&display=swap">
<style>
  :root {
    --sheet: #ffffff;
    --cyan: #00bbe4;
    --navy: #0568ab;
    --deep: #0a5fa3;
    --white: #ffffff;
    --trim: #bdbdbd;
  }
  * { margin: 0; padding: 0; box-sizing: border-box; }
  html, body { width: 1200px; height: 900px; overflow: hidden; background: var(--sheet); }
  body { font-family: "Barlow", Arial, sans-serif; }

  .sheet { position: relative; width: 1200px; height: 900px; }

  .crop-marks { position: absolute; inset: 0; }

  .card { position: absolute; width: 360px; height: 232px; overflow: hidden; }
  .card--front-cyan { left: 236px; top: 209px; background: var(--cyan); }
  .card--back-details { left: 604px; top: 209px; background: var(--navy); }
  .card--front-white { left: 236px; top: 453px; background: var(--white); border: 2px solid var(--cyan); }
  .card--back-name { left: 604px; top: 453px; background: var(--navy); }

  .wordmark { position: absolute; font-weight: 800; white-space: nowrap; letter-spacing: -0.5px; }
  .card--front-cyan .wordmark { right: 52px; top: 116px; font-size: 22px; color: var(--deep); }
  .card--front-white .wordmark { left: 0; right: 0; top: 124px; text-align: center; font-size: 30px; color: var(--deep); }

  .wordmark-dot { position: absolute; border-radius: 50%; }
  .card--front-cyan .wordmark-dot { right: 96px; top: 74px; width: 30px; height: 30px; background: var(--deep); }
  .card--front-white .wordmark-dot { left: 158px; top: 68px; width: 40px; height: 40px; background: var(--cyan); }

  .details { position: absolute; left: 56px; top: 78px; color: var(--white); }
  .details__name { font-size: 12.5px; font-weight: 400; letter-spacing: 1px; line-height: 14px; }
  .role { font-size: 5.5px; font-weight: 800; letter-spacing: 1px; text-transform: uppercase; }
  .details .role { margin-top: 2px; }
  .company { font-size: 5.5px; font-weight: 800; letter-spacing: 1.2px; color: var(--cyan); text-transform: uppercase; }
  .details .company { margin-top: 10px; }
  .details__line { font-size: 6px; color: var(--cyan); line-height: 9px; }
  .web { font-size: 6px; font-weight: 700; color: var(--white); }
  .details .web { margin-top: 7px; }

  .signature { position: absolute; left: 0; right: 0; top: 88px; text-align: center; color: var(--white); }
  .signature__phone { font-size: 9.5px; color: var(--cyan); letter-spacing: 0.5px; }
  .signature__name { font-size: 19px; font-weight: 400; letter-spacing: 1.6px; line-height: 19px; }
  .signature__domain { font-size: 9.5px; color: var(--cyan); line-height: 11px; }
  .signature .role { margin-top: 9px; }

  .footer { position: absolute; left: 0; right: 0; top: 197px; text-align: center; line-height: 9px; }
</style>
</head>
<body>
<main class="sheet">
  <svg class="crop-marks" width="1200" height="900" viewBox="0 0 1200 900" aria-hidden="true">
    <g stroke="var(--trim)" stroke-width="1">
      <line x1="244.5" y1="178" x2="244.5" y2="209"/>
      <line x1="588.5" y1="178" x2="588.5" y2="209"/>
      <line x1="612.5" y1="178" x2="612.5" y2="209"/>
      <line x1="956.5" y1="178" x2="956.5" y2="209"/>
      <line x1="244.5" y1="685" x2="244.5" y2="722"/>
      <line x1="588.5" y1="685" x2="588.5" y2="722"/>
      <line x1="612.5" y1="685" x2="612.5" y2="722"/>
      <line x1="956.5" y1="685" x2="956.5" y2="722"/>
      <line x1="204" y1="217.5" x2="236" y2="217.5"/>
      <line x1="204" y1="433.5" x2="236" y2="433.5"/>
      <line x1="204" y1="461.5" x2="236" y2="461.5"/>
      <line x1="204" y1="677.5" x2="236" y2="677.5"/>
      <line x1="964" y1="217.5" x2="996" y2="217.5"/>
      <line x1="964" y1="433.5" x2="996" y2="433.5"/>
      <line x1="964" y1="461.5" x2="996" y2="461.5"/>
      <line x1="964" y1="677.5" x2="996" y2="677.5"/>
    </g>
  </svg>

  <section class="card card--front-cyan">
    <span class="wordmark-dot"></span>
    <p class="wordmark">Kestrel Sound</p>
  </section>

  <section class="card card--back-details">
    <div class="details">
      <p class="details__name">Bartholomew Quenneville</p>
      <p class="role">Audio Engineer</p>
      <p class="company">Kestrel Sound</p>
      <p class="details__line">Telephone 0478 615 027</p>
      <p class="details__line">Email bartholomew@kestrelsound.com.au</p>
      <p class="web">www.kestrelsound.com.au</p>
    </div>
  </section>

  <section class="card card--front-white">
    <span class="wordmark-dot"></span>
    <p class="wordmark">Kestrel Sound</p>
  </section>

  <section class="card card--back-name">
    <div class="signature">
      <p class="signature__phone">Phone 0478 615 027</p>
      <p class="signature__name">bartholomew</p>
      <p class="signature__domain">@kestrelsound.com.au</p>
      <p class="role">Audio Engineer</p>
    </div>
    <div class="footer">
      <p class="company">Kestrel Sound</p>
      <p class="web">www.kestrelsound.com.au</p>
    </div>
  </section>
</main>
</body>
</html>
```